Business Card & Logo Design Project

I am looking for a slick/simple design for a logo and business card, for a music Producer/Mixer/Engineer.

I'm based in Tokyo, Japan and I help my clients polish up their creation to major radio/TV status. My clients pay me for my taste, sense of balance expertise and creative direction/

Design should give impression of seal of quality, professionalism, and enthusiasm need some sort of a logo like design for "vantrix productions".

Please don't include music notes or instruments or anything musically related and anything samurai or ninja or too much Japan in them on the design.

I like clever, slick stuff that's not too obvious.
I also like a smooth gradation type transition. My favorite color is deep dark blue/

Good Luck and Thank you for your effort.
Updates

I would like a two-sided design for this one.
One side with "vantrix productions" (all lower case) on, and the other side with my name and contact info.

Please also consider portrait position (or direction).  (as opposed to landscape) 

Target Market(s)

My primary targets are artists & bands, who want absolute best for their creation.

Industry/Entity Type

Business

Requirements
Must have
• Two-Sided
1, vantrix productions
2, Kenji Harumoto, Producer/Mixer/Engineer, +81 090 4827 3516, brambleway@mailnest.example
Nice to have
• Any suggestions are welcome//
Should not have
• Anything music related images.
(e.g. CD, music notations, instruments etc.)

```html
<!DOCTYPE html>
<html lang="en">
<head>
<meta charset="utf-8">
<title>vantrix productions – business card</title>
<link rel="stylesheet" href="https://fonts.googleapis.com/css2?family=Sue+Ellen+Francisco&display=swap">
<style>
  :root {
    --page: #ffffff;
    --card-front: #ffffff;
    --card-back: #03154d;
    --ink-navy: #2a3566;
    --ink-light: #ececec;
    --ink-grey: #8d8d8d;
    --rule: #111111;
    --tone-navy: #2b3a6b;
    --tone-green: #1f7a2c;
    --tone-red: #cf2f3a;
    --tone-yellow: #f4dc3a;
    --tone-orange: #d57a1c;
    --tone-slate: #6b7080;
  }
  html, body {
    margin: 0;
    width: 1200px;
    height: 969px;
    overflow: hidden;
    background: var(--page);
    font-family: "Sue Ellen Francisco", cursive;
  }
  .stage { position: relative; width: 1200px; height: 969px; }
  .card {
    position: absolute;
    top: 103px;
    width: 432px;
    height: 755px;
    overflow: hidden;
  }
  .card--front {
    left: 140px;
    background: var(--card-front);
    box-shadow: 0 2px 14px rgba(0,0,0,0.35);
  }
  .card--back { left: 660px; background: var(--card-back); }

  .wordmark {
    position: absolute;
    right: 22px;
    top: 30px;
    margin: 0;
    font-size: 62px;
    font-weight: 400;
    line-height: 1;
    color: var(--ink-navy);
    white-space: nowrap;
  }
  .shape-cluster {
    position: absolute;
    left: 12px;
    top: 496px;
    width: 336px;
    height: 252px;
  }
  .rule {
    position: absolute;
    left: 0;
    height: 2px;
    background: var(--rule);
  }
  .card--front .rule { top: 697px; width: 432px; }
  .card--back .rule { top: 272px; width: 432px; height: 2px; }

  .holder-name {
    position: absolute;
    left: 130px;
    top: 268px;
    margin: 0;
    font-size: 52px;
    font-weight: 400;
    color: var(--ink-light);
    background: var(--card-back);
    padding: 0 4px;
    white-space: nowrap;
  }
  .contact {
    position: absolute;
    right: 26px;
    top: 578px;
    margin: 0;
    text-align: right;
    font-style: normal;
    line-height: 1.12;
  }
  .contact__role { display: block; font-size: 38px; color: var(--ink-grey); }
  .contact__line { display: block; font-size: 40px; color: var(--ink-light); }
</style>
</head>
<body>
<main class="stage">
  <section class="card card--front" aria-label="Card front">
    <h1 class="wordmark">vantrix productions</h1>
    <svg class="shape-cluster" viewBox="0 0 336 252" role="img" aria-label="Overlapping translucent coloured geometric shapes in navy, green, red and yellow">
      <defs>
        <linearGradient id="clusterTones" x1="0" y1="1" x2="1" y2="0">
          <stop offset="0" stop-color="var(--tone-red)" stop-opacity="0.85"/>
          <stop offset="0.3" stop-color="var(--tone-yellow)" stop-opacity="0.8"/>
          <stop offset="0.55" stop-color="var(--tone-green)" stop-opacity="0.8"/>
          <stop offset="0.8" stop-color="var(--tone-navy)" stop-opacity="0.9"/>
          <stop offset="1" stop-color="var(--tone-slate)" stop-opacity="0.6"/>
        </linearGradient>
      </defs>
      <rect x="0" y="0" width="336" height="252" rx="40" fill="url(#clusterTones)" opacity="0.55"/>
    </svg>
    <div class="rule"></div>
  </section>

  <section class="card card--back" aria-label="Card back">
    <div class="rule"></div>
    <h2 class="holder-name">Kenji Harumoto</h2>
    <address class="contact">
      <span class="contact__role">Producer/Mixer/Engineer</span>
      <span class="contact__line">+81 090 4827 3516</span>
      <span class="contact__line">brambleway@mailnest.example</span>
    </address>
  </section>
</main>
</body>
</html>
```